Real estate Agent postcards for homeowners

I need a "Just Sold" postcard for two real agents , I am providing pictures of the agents and neighborhood.
I have the front and back of a postcard containing the information I want on the postcard.
I want a designer to take the info and pictures and design a new postcard and choose the colors

Target Market(s)

homeowners of luxury condos

Industry/Entity Type

Real Estate Agent

Colors

Designer to choose colors to be used in the design.

```html
<!DOCTYPE html>
<html lang="en">
<head>
<meta charset="utf-8">
<title>Just Sold – Bayside Realtors</title>
<link href="https://fonts.googleapis.com/css2?family=Catamaran:wght@300;400;600;700;800&family=Zilla+Slab:ital,wght@1,700&display=swap" rel="stylesheet">
<style>
  :root{
    --blue-deep:#0f3f6e;
    --blue-mid:#1f5b91;
    --blue-light:#3b7db5;
    --gold:#d8bc6c;
    --gold-dark:#b89a4c;
    --white:#ffffff;
    --ink:#17467a;
  }
  *{margin:0;padding:0;box-sizing:border-box}
  html,body{width:1200px;height:857px;overflow:hidden;background:#fff}
  body{font-family:"Catamaran",sans-serif;color:var(--white)}
  .postcard{position:relative;width:1200px;height:857px;overflow:hidden;
    background:linear-gradient(180deg,var(--blue-mid) 0%,var(--blue-deep) 100%)}
  .line{position:absolute;line-height:1;white-space:nowrap}

  /* header */
  .masthead{position:absolute;left:0;top:0;width:1200px;height:151px;
    background:radial-gradient(ellipse at 45% 60%,var(--blue-light) 0%,var(--blue-mid) 45%,var(--blue-deep) 100%)}
  .masthead__title{position:absolute;left:34px;top:23px;font-family:"Zilla Slab",serif;
    font-style:italic;font-weight:700;font-size:128px;line-height:1;color:var(--gold);
    letter-spacing:3px;white-space:nowrap;text-shadow:0 3px 6px rgba(0,0,0,.25)}
  .masthead__place{left:604px;top:99px;font-style:italic;font-size:30px;font-weight:400}

  /* listings band */
  .listings{position:absolute;left:0;top:151px;width:1200px;height:362px;border-top:2px solid #e9eef4}
  .photo{position:absolute;top:0;height:100%}
  .photo--garden{left:0;width:540px;background:linear-gradient(180deg,#9fc6e8 0%,#3f77ae 30%,#5b8f3c 55%,#b3452f 80%,#7a4a2a 100%)}
  .photo--terrace{right:0;width:520px;background:linear-gradient(160deg,#8ab7de 0%,#4b7c9e 30%,#6d8a4a 50%,#a55e3e 75%,#6e4a3a 100%)}
  .listings__panel{position:absolute;left:0;top:0}
  .sale__address{font-size:24px;font-weight:600}
  .sale__address small{font-size:19px;font-weight:400}
  .sale__rooms{font-size:24px;font-weight:300}
  .sale__area{font-size:23px;font-weight:400}
  .sale__rule{position:absolute;border-top:2px dotted rgba(255,255,255,.75)}
  .sale__price{font-size:21px;font-weight:400}
  .sale__price b{font-weight:800;font-size:23px}
  .marker{position:absolute;width:34px;height:34px}

  /* brand strip */
  .brand-strip{position:absolute;left:0;top:516px;width:1200px;height:48px;background:var(--blue-deep)}
  .brand-strip__tagline{left:566px;top:529px;font-style:italic;font-size:27px;font-weight:400}
  .brand-strip__tagline b{font-weight:800;font-size:31px}
  .brand-tab{position:absolute;left:0;top:516px}
  .brand-tab__name{left:20px;top:537px;font-weight:800;font-size:42px;letter-spacing:.5px;color:var(--ink)}

  /* agents */
  .agent__name{font-weight:700;font-size:28px;letter-spacing:.5px;top:650px}
  .agent__rule{position:absolute;top:686px;border-top:2px dotted rgba(255,255,255,.7)}
  .agent__phone{font-weight:300;font-size:32px;top:703px}
  .agent__email{font-weight:400;font-size:21px;top:740px}
  .agent__unit{font-weight:700;font-size:26px;color:var(--gold);top:768px}
  .agent--left{right:748px;text-align:right}
  .agent--right{left:950px}
  .portrait-frame{position:absolute;top:580px;width:213px;height:214px;background:rgba(120,160,200,.35);padding:9px 8px}
  .portrait-frame--left{left:474px}
  .portrait-frame--right{left:720px}
  .portrait{width:100%;height:100%;border:2px solid #fff}
  .portrait--left{background:linear-gradient(180deg,#c9a98a,#d7b98a 60%,#6fc6d8)}
  .portrait--right{background:linear-gradient(180deg,#6fa6d6,#2f6fa8 60%,#1f3a66)}

  /* footer */
  .footer{position:absolute;left:0;top:812px;width:1200px;height:45px;
    background:linear-gradient(90deg,var(--gold-dark),var(--gold) 50%,var(--gold-dark))}
  .footer__site{right:32px;top:826px;font-size:21px;font-weight:400}
</style>
</head>
<body>
<main class="postcard">

  <header class="masthead">
    <h1 class="masthead__title">Just Sold!</h1>
  </header>
  <p class="line masthead__place">In Seabright Cove</p>

  <section class="listings">
    <div class="photo photo--garden" role="img" aria-label="Ocean view over a green lawn and flower beds from a terrace railing"></div>
    <div class="photo photo--terrace" role="img" aria-label="Sunny terrace with patio chairs overlooking the bay and hillside palms"></div>

    <svg class="listings__panel" width="1200" height="362" viewBox="0 0 1200 362">
      <defs>
        <linearGradient id="panelGold" x1="0" y1="0" x2="1" y2="1">
          <stop offset="0" stop-color="#c9ab5e"/>
          <stop offset="1" stop-color="#b8994c"/>
        </linearGradient>
      </defs>
      <polygon points="488,0 885,0 732,362 332,362" fill="url(#panelGold)"/>
    </svg>

    <svg class="marker" style="left:457px;top:14px" viewBox="0 0 34 34" aria-hidden="true">
      <circle cx="17" cy="17" r="15" fill="#1f5b91" stroke="#ffffff" stroke-width="2"/>
      <polygon points="22,9 22,25 10,17" fill="#e7cf85"/>
    </svg>
    <p class="line sale__address" style="left:504px;top:21px">43, Vista Marina <small>in Building 13</small></p>
    <p class="line sale__rooms" style="right:426px;top:53px">3 bedrooms, 2 bathrooms</p>
    <p class="line sale__area" style="left:482px;top:82px">1,840 Sq.ft.</p>
    <div class="sale__rule" style="left:476px;top:109px;width:304px"></div>
    <p class="line sale__price" style="right:420px;top:124px">Sold for <b>$1,000,000</b> <i>buyer side</i></p>

    <p class="line sale__address" style="right:444px;top:227px">80, Vista Marina <small>in Building 8</small></p>
    <svg class="marker" style="left:766px;top:220px" viewBox="0 0 34 34" aria-hidden="true">
      <circle cx="17" cy="17" r="15" fill="#1f5b91" stroke="#ffffff" stroke-width="2"/>
      <polygon points="12,9 12,25 24,17" fill="#e7cf85"/>
    </svg>
    <p class="line sale__rooms" style="right:464px;top:259px">1 bedroom, 2 bathrooms</p>
    <p class="line sale__area" style="right:476px;top:288px">985 Sq.ft.</p>
    <div class="sale__rule" style="left:480px;top:318px;width:232px"></div>
    <p class="line sale__price" style="right:492px;top:330px">Sold for <b>$769,000</b> <i>seller side</i></p>
  </section>

  <div class="brand-strip"></div>
  <p class="line brand-strip__tagline">We’re local agents and your neighbors. <b>Call US!</b></p>
  <svg class="brand-tab" width="490" height="72" viewBox="0 0 490 72" aria-hidden="true">
    <path d="M0,0 L488,0 Q470,0 458,30 Q445,72 400,72 L0,72 Z" fill="#ffffff"/>
  </svg>
  <p class="line brand-tab__name">BAYSIDE REALTORS</p>

  <h2 class="line agent__name agent--left">MAREN WHITFIELD</h2>
  <div class="agent__rule" style="left:206px;width:246px"></div>
  <p class="line agent__phone agent--left">(310) 555-0148</p>
  <p class="line agent__email agent--left">SalesbyMaren@example.com</p>
  <p class="line agent__unit agent--left">Unit 12-40</p>

  <div class="portrait-frame portrait-frame--left">
    <div class="portrait portrait--left" role="img" aria-label="Portrait photo of agent Maren Whitfield"></div>
  </div>
  <div class="portrait-frame portrait-frame--right">
    <div class="portrait portrait--right" role="img" aria-label="Portrait photo of agent Theo Vance by the sea"></div>
  </div>

  <h2 class="line agent__name agent--right">THEO VANCE</h2>
  <div class="agent__rule" style="left:950px;width:232px"></div>
  <p class="line agent__phone agent--right">(650) 555-0192</p>
  <p class="line agent__email agent--right">TheoVance@example.com</p>
  <p class="line agent__unit agent--right">Unit 6-22</p>

  <footer class="footer"></footer>
  <p class="line footer__site">www.BaysideRealtors.com</p>
</main>
</body>
</html>
```